Brochure Design Oakridge Capital Partners

Create a brochure, which sells my business. Utilise the website www.oakridgecapitalpartners.example for the details that need to go into the brochure. I would like 2 designs, one for a 4 page brochure and the other for a two page brochure (focus firstly on the 4 page).

The focus points are our 4 year rent guarantee and also out pitch that we are invested with them. Please see the website.

Need to focus on the main points as per the website, can use text from the website and the graphics where suitable.

On the 4 page brochure, first 3 pages to be info as per the website. On the 4 page of the brochure I would like the information included on the final 2 pages of the attached document (the investment property example). Please shrink this down, you do not need to include all the wording more so the figures.

The colours of the brochure to be blue, white and black

Target Market(s)

Property Investors

Industry/Entity Type

Business

Colors
0355a3
ffffff

Requirements
Must have
• Must have the main info on the website, (4 year rent guarantee) 'We are invested with you'
Nice to have
• Professional look

```html
<!DOCTYPE html>
<html lang="en">
<head>
<meta charset="utf-8">
<title>Oakridge Capital Partners – Brochure Spread</title>
<link href="https://fonts.googleapis.com/css2?family=Oswald:wght@500;600&family=Lato:wght@400;700;900&family=Montserrat:wght@700;800&display=swap" rel="stylesheet">
<style>
  :root{
    --brand-blue:#0355a3;
    --deep-blue:#073f86;
    --sky-blue:#00b7e6;
    --debt-red:#e8000b;
    --white:#ffffff;
    --ink:#111111;
    --navy-text:#0a3d7a;
    --paper-grey:#eceef1;
    --backdrop:#d9dadc;
  }
  *{box-sizing:border-box;margin:0;padding:0}
  html,body{width:1200px;height:995px;overflow:hidden;background:var(--backdrop)}
  body{font-family:"Lato",sans-serif;position:relative}

  .page{position:absolute;top:110px;width:548px;height:775px;overflow:hidden;box-shadow:0 6px 18px rgba(0,0,0,.18)}
  .page--back{left:54px;background:linear-gradient(160deg,#0a61b8 0%,var(--brand-blue) 45%,var(--deep-blue) 100%);border:8px solid var(--white)}
  .page--cover{left:602px;background:linear-gradient(180deg,#f4f5f7 0%,var(--paper-grey) 100%)}

  /* back page */
  .section-banner{position:absolute;left:0;height:34px;background:var(--white);clip-path:polygon(0 0,100% 0,92% 100%,0 100%);
    font-family:"Montserrat",sans-serif;font-weight:800;font-size:16px;letter-spacing:2px;color:var(--brand-blue);padding:8px 0 0 22px}
  .section-banner--example{top:52px;width:390px}
  .section-banner--growth{top:322px;width:300px}
  .intro{position:absolute;left:22px;width:480px;color:var(--white);font-size:11.5px;line-height:1.5;letter-spacing:.4px}
  .intro--example{top:100px}
  .intro--growth{top:370px}

  .costs{position:absolute;left:22px;top:165px;width:420px;color:var(--white)}
  .costs__head{display:flex;align-items:flex-end}
  .costs__title{background:var(--white);color:var(--brand-blue);font-size:17px;letter-spacing:1px;padding:4px 10px;width:230px}
  .costs__currency{background:#1a8ee0;color:var(--white);font-weight:700;font-size:15px;width:52px;text-align:center;padding:4px 0;margin-left:2px;align-self:stretch}
  .costs__row{display:flex;align-items:center;font-size:12px;letter-spacing:.8px;margin-top:8px}
  .costs__label{width:70px}
  .costs__rule{width:160px;height:1px;background:rgba(255,255,255,.8);margin-right:12px}
  .costs__value{font-size:12.5px}
  .costs__note{font-size:7px;line-height:1.1;margin-left:6px}
  .costs__footnote{font-size:12px;letter-spacing:.8px;margin-top:10px}

  .legend{position:absolute;right:40px;top:418px;color:var(--white);font-size:9px;line-height:1.3}
  .legend__item{display:flex;align-items:flex-start;gap:4px}
  .legend__swatch{width:6px;height:6px;margin-top:3px}
  .growth-chart{position:absolute;left:14px;top:455px}
  .growth-chart text{font-family:"Lato",sans-serif;fill:var(--white)}

  /* cover page */
  .tagline{position:absolute;left:22px;top:22px;width:232px;height:168px;background:rgba(3,85,163,.92);z-index:2;
    font-family:"Oswald",sans-serif;font-weight:600;color:var(--white);font-size:34px;line-height:1.08;letter-spacing:2.5px;padding:22px 0 0 26px}
  .brand{position:absolute;right:24px;top:38px;display:flex;align-items:center;gap:9px}
  .brand__mark{width:22px;height:22px;background:var(--brand-blue)}
  .brand__name{font-family:"Lato",sans-serif;font-weight:900;font-size:17px;color:var(--ink)}
  .hero-photo{position:absolute;left:0;top:100px;width:548px;height:408px;
    background:linear-gradient(135deg,#c9d2da 0%,#9aa7b3 35%,#5c6670 60%,#b9c4cf 100%)}
  .web-tab{position:absolute;left:40px;top:472px;width:270px;height:36px;background:var(--brand-blue);z-index:2;
    color:var(--white);font-size:12px;letter-spacing:.6px;padding:11px 0 0 14px}
  .hero-rule{position:absolute;left:0;top:506px;width:548px;height:3px;background:#1a8ee0}
  .contact{position:absolute;left:40px;top:538px;color:var(--ink)}
  .contact__title{font-family:"Oswald",sans-serif;font-weight:600;font-size:19px;letter-spacing:1.5px;color:var(--navy-text);margin-bottom:12px}
  .contact__line{display:flex;align-items:flex-start;gap:8px;font-size:12.5px;letter-spacing:.8px;line-height:1.55}
  .contact__phone{font-size:22px;letter-spacing:1.5px;font-weight:700;margin:6px 0 4px;align-items:center}
  .contact__line svg{flex:none;margin-top:3px}
  .cover-strip{position:absolute;left:0;bottom:0;width:548px;height:12px;background:linear-gradient(90deg,var(--brand-blue),#1a8ee0)}
</style>
</head>
<body>

<section class="page page--back" aria-label="Investment property example page">
  <h2 class="section-banner section-banner--example">INVESTMENT PROPERTY EXAMPLE</h2>
  <p class="intro intro--example">The below example is based on an investment property that Oakridge Capital Partners had available through one of their partners in 2016. It is representative of similar properties currently available through Oakridge Capital Partners. Property Facts;</p>

  <div class="costs">
    <div class="costs__head"><span class="costs__title">Initial Costs</span><span class="costs__currency">$</span></div>
    <div class="costs__row"><span class="costs__label">Stamp Duty</span><span class="costs__rule"></span><span class="costs__value">6,294</span><span class="costs__note">(land value<br>$212,000)</span></div>
    <div class="costs__row"><span class="costs__label">Solicitor</span><span class="costs__rule"></span><span class="costs__value">1,200</span></div>
    <div class="costs__row"><span class="costs__label">TOTAL</span><span class="costs__rule"></span><span class="costs__value">7,494*</span></div>
    <p class="costs__footnote">*estimate only</p>
  </div>

  <h2 class="section-banner section-banner--growth">GROWTH PROJECTION</h2>
  <p class="intro intro--growth">Whilst capital growth is never a guarantee in the short term, in the long term history has shown one undeniable fact, property prices in Australian capital cities and major metropolitan areas increase in value.</p>

  <div class="legend">
    <div class="legend__item"><span class="legend__swatch" style="background:var(--debt-red)"></span>Debt</div>
    <div class="legend__item"><span class="legend__swatch" style="background:var(--sky-blue)"></span>Capital<br>Gain</div>
  </div>

  <svg class="growth-chart" width="510" height="300" viewBox="0 0 510 300" aria-label="Growth projection bar chart">
    <g font-size="11" text-anchor="end" letter-spacing=".8">
      <text x="95" y="284">0</text>
      <text x="95" y="241">250,000</text>
      <text x="95" y="198">500,000</text>
      <text x="95" y="155">750,000</text>
      <text x="95" y="112">1,000,000</text>
      <text x="95" y="69">1,250,000</text>
      <text x="95" y="26">1,500,000</text>
    </g>
    <line x1="115" y1="18" x2="115" y2="272" stroke="#fff" stroke-width="1" stroke-dasharray="3 3"/>
    <circle cx="115" cy="14" r="5" fill="none" stroke="#fff"/>
    <path d="M112 14h6M115 11v6" stroke="#fff"/>
    <circle cx="115" cy="276" r="5" fill="none" stroke="#fff"/>
    <path d="M112 276h6" stroke="#fff"/>
    <!-- baseline y=280, 1,500,000 => 258px -->
    <rect x="150" y="228" width="30" height="52" fill="var(--debt-red)"/>
    <rect x="220" y="222" width="22" height="58" fill="var(--debt-red)"/>
    <rect x="234" y="170" width="28" height="110" fill="var(--sky-blue)"/>
    <rect x="300" y="215" width="22" height="65" fill="var(--debt-red)"/>
    <rect x="314" y="134" width="30" height="146" fill="var(--sky-blue)"/>
    <rect x="380" y="206" width="22" height="74" fill="var(--debt-red)"/>
    <rect x="394" y="92" width="30" height="188" fill="var(--sky-blue)"/>
    <rect x="460" y="197" width="22" height="83" fill="var(--debt-red)"/>
    <rect x="474" y="40" width="30" height="240" fill="var(--sky-blue)"/>
    <g font-size="10" text-anchor="middle" letter-spacing=".6">
      <text x="165" y="294">Current</text>
      <text x="245" y="294">5 years</text>
      <text x="325" y="294">10 years</text>
      <text x="405" y="294">15 years</text>
      <text x="485" y="294">20 years</text>
    </g>
  </svg>
</section>

<section class="page page--cover" aria-label="Brochure cover">
  <h1 class="tagline">WE ARE<br>INVESTED<br>WITH YOU</h1>
  <div class="brand"><span class="brand__mark"></span><span class="brand__name">Oakridge Capital Partners</span></div>
  <div class="hero-photo" role="img" aria-label="Photo of a smiling couple on a sofa reviewing property documents with an adviser"></div>
  <div class="web-tab">www.oakridgecapitalpartners.example</div>
  <div class="hero-rule"></div>

  <address class="contact" style="font-style:normal">
    <h2 class="contact__title">CONTACT US</h2>
    <div class="contact__line">
      <svg width="10" height="13" viewBox="0 0 10 13"><path d="M5 12.5C2 8.5 1 6.8 1 5a4 4 0 0 1 8 0c0 1.8-1 3.5-4 7.5z" fill="none" stroke="#111" stroke-width="1.2"/><circle cx="5" cy="5" r="1.5" fill="#111"/></svg>
      <span>Level 3, 18 Harbourview Place, Castle Ridge NSW 2160<br>Australia</span>
    </div>
    <div class="contact__line contact__phone">
      <svg width="16" height="16" viewBox="0 0 16 16" style="margin-top:0"><path d="M3.5 1.5l2.5 3-1.5 2c.8 1.8 2.3 3.3 4.1 4.1l2-1.5 3 2.5-1.6 2.4C6.5 14 2 9.5 1.1 3.1z" fill="#111"/></svg>
      <span>1300 555 017</span>
    </div>
    <div class="contact__line">
      <svg width="11" height="9" viewBox="0 0 11 9"><rect x=".5" y=".5" width="10" height="8" fill="none" stroke="#111"/><path d="M.5 .5l5 4.5 5-4.5" fill="none" stroke="#111"/></svg>
      <span>admin@oakridgecapitalpartners.example</span>
    </div>
  </address>
  <div class="cover-strip"></div>
</section>

</body>
</html>
```